We need motivational posters designed to be used in classrooms at a truck driving school. The purpose of the posters is to motivate the students.

I want the the quotes to be the main focal point of emphasis and our logo on the bottom of the poster for branding purposes.

I would like the images to be related to the trucking industry

Below are the quotes for the posters

Poster 1
"Start where you are. Use what you have. Do what you can."
-Delmar Quisby-

Poster 2
"The secret of getting ahead is getting started"
-Owen Farrow-

Poster 3
"Most effective way to do it, is to do it."
-Rosalind Pemberly-

Poster 4
"Set your goals big, and don't stop till you get there."
-Cy Whitlock-

Poster 5
"If you are not willing to learn, no one can help you. If you are determined to learn, no one can stop you."
-Unknown-

Poster 6
"The will to succeed is important, but what's more important is the will to prepare."
-Dougie Hallam-

THESE POSTERS SHOULD BE DESIGNED AS 18X24
LANDSCAPE AND PORTRAIT ORIENTATION

Industry/Entity Type

School

```html
<!DOCTYPE html>
<html lang="en">
<head>
<meta charset="utf-8">
<title>Poster 6 – The Will to Prepare</title>
<link rel="stylesheet" href="https://fonts.googleapis.com/css2?family=Libre+Bodoni:wght@700&family=Archivo:wght@400;600&display=swap">
<style>
  :root {
    --ink: #111111;
    --paper: #ffffff;
    --sky-top: #e4e6e8;
    --sky-mid: #d8dbdd;
    --sky-low: #c9cdd0;
    --hills: #5f5852;
    --ground-dark: #6f6556;
    --ground: #8c8170;
    --road-edge: #55585c;
    --road: #3f4246;
    --road-deep: #36393d;
    --brand-dark: #1a1a1a;
  }
  * { margin: 0; padding: 0; box-sizing: border-box; }
  html, body {
    width: 1200px;
    height: 900px;
    overflow: hidden;
    background: var(--paper);
  }
  .poster {
    position: relative;
    width: 1200px;
    height: 900px;
    background: var(--paper);
  }
  .scene {
    position: absolute;
    left: 0;
    top: 0;
    width: 1200px;
    height: 800px;
    background: linear-gradient(
      to bottom,
      var(--sky-top) 0%,
      var(--sky-mid) 30%,
      var(--sky-low) 50%,
      var(--hills) 55%,
      var(--ground-dark) 59%,
      var(--ground) 66%,
      var(--road-edge) 74%,
      var(--road) 84%,
      var(--road-deep) 100%
    );
  }
  .quote {
    position: absolute;
    left: 40px;
    top: 66px;
    font-family: "Libre Bodoni", "Bodoni Moda", serif;
    font-weight: 700;
    font-size: 62px;
    line-height: 67px;
    word-spacing: 5px;
    color: var(--ink);
    white-space: nowrap;
  }
  .author {
    position: absolute;
    left: 41px;
    top: 311px;
    font-family: "Archivo", sans-serif;
    font-weight: 400;
    font-size: 31px;
    letter-spacing: 0.3px;
    color: var(--ink);
    text-transform: uppercase;
  }
  .brand {
    position: absolute;
    left: 40px;
    top: 820px;
    height: 60px;
    display: flex;
    align-items: center;
    gap: 10px;
  }
  .brand-mark {
    width: 60px;
    height: 60px;
    border-radius: 50%;
    background: var(--brand-dark);
  }
  .brand-name {
    font-family: "Archivo", sans-serif;
    font-weight: 600;
    font-size: 20px;
    color: var(--brand-dark);
  }
</style>
</head>
<body>
  <main class="poster">
    <div class="scene" role="img" aria-label="Photograph of an empty open highway stretching into the distance through a wide valley between snow-dusted hills under an overcast grey sky"></div>

    <blockquote class="quote">
      The will to succeed is important,<br>
      but what's more important is<br>
      the will to prepare.
    </blockquote>
    <p class="author">Dougie Hallam</p>

    <footer class="brand">
      <span class="brand-mark"></span>
      <span class="brand-name">Summit Haul Driving School</span>
    </footer>
  </main>
</body>
</html>
```